Pinecrest Motor Lending- Free Oil Change letters

this is A Letter from my Used Car Sales & Service business. Specifically this is in a large window envelope (See Web Links) A free oil change to get this specific customer to open the envelope. The free oil change is the top have of the letter stuff in 4 1/8 x 9 open window envelope. The rest of letter is to the Fresh bankruptcy people. The coupon is to get them to open and read my offer. I had the combined ideas from the moving target link attached.
the middle of the envelope has to have a customer name address for postal delivery
I have also included our company website and our logo to be contained. This has to be in a letter program that I will mail merge a database mailer to print.

This project is for only what will be view through the large window envelope

my company website
http://www.pmlndx.com/

envelope I use
http://www.mailerpackdepot.com/sleeves/pane/wide-pane/sleeve-73915.html

Envelope Dimensions: 4 1/8 x 9 1/2
Window Dimensions: 3 x 8 (From Left Edge: 3/4 - From Bottom Edge: 1/2)

the whole point is the make this look highend to get the customer to want read the letter.. The Letter will talk about We are the Second Change Credit Expert and to come to us to buy a used car.

Reason: Looking for so more designs

Reason: narrowing the designs and making revisions

```html
<!DOCTYPE html>
<html lang="en">
<head>
<meta charset="utf-8">
<title>Pinecrest Motor Lending – Free Oil Change Insert</title>
<link rel="stylesheet" href="https://fonts.googleapis.com/css2?family=Alfa+Slab+One&family=Questrial&display=swap">
<style>
  :root {
    --page-bg: #ececec;
    --card-dark: #1b1b1d;
    --card-dark-2: #2a2a2d;
    --headline-white: #ffffff;
    --headline-yellow: #f6c400;
    --accent-yellow: #f2c200;
    --red-deep: #7c1013;
    --red-mid: #b3201f;
    --red-light: #d9463c;
    --window-fill: rgba(255, 255, 255, 0.82);
    --window-line: #3a3a3a;
  }
  * { margin: 0; padding: 0; box-sizing: border-box; }
  html, body {
    width: 1200px;
    height: 657px;
    overflow: hidden;
    background: var(--page-bg);
  }
  .insert {
    position: absolute;
    left: 42px;
    top: 70px;
    width: 1116px;
    height: 516px;
    overflow: hidden;
    background: radial-gradient(ellipse at 40% 35%, var(--card-dark-2), var(--card-dark) 70%);
    box-shadow: 0 6px 18px rgba(0, 0, 0, 0.25);
  }
  .insert__waves {
    position: absolute;
    left: 0;
    top: 0;
    width: 1116px;
    height: 516px;
  }
  .headline {
    position: absolute;
    left: 52px;
    font-family: "Alfa Slab One", serif;
    line-height: 1;
    letter-spacing: 2px;
    text-shadow: 0 0 4px rgba(200, 40, 20, 0.7), 0 2px 0 rgba(120, 20, 10, 0.8);
  }
  .headline--free {
    top: 58px;
    font-size: 160px;
    color: var(--headline-white);
  }
  .headline--offer {
    top: 222px;
    font-size: 66px;
    color: var(--headline-yellow);
  }
  .dealer-contact {
    position: absolute;
    right: 262px;
    top: 72px;
    text-align: right;
    font-family: "Questrial", sans-serif;
    font-size: 17px;
    line-height: 21px;
    color: var(--accent-yellow);
  }
  .dealer-brand {
    position: absolute;
    left: 862px;
    top: 80px;
    display: flex;
    align-items: center;
    gap: 10px;
  }
  .dealer-brand__mark {
    width: 34px;
    height: 34px;
    background: var(--accent-yellow);
    flex-shrink: 0;
  }
  .dealer-brand__name {
    font-family: "Questrial", sans-serif;
    font-size: 21px;
    line-height: 24px;
    color: var(--accent-yellow);
    width: 180px;
  }
  .address-window {
    position: absolute;
    left: 53px;
    top: 302px;
    width: 426px;
    height: 146px;
    border-radius: 18px;
    background: var(--window-fill);
    padding: 36px 40px 0;
  }
  .address-window__line {
    height: 1px;
    background: var(--window-line);
    margin-bottom: 33px;
  }
  .vehicle-photo {
    position: absolute;
    left: 586px;
    top: 210px;
    width: 490px;
    height: 258px;
    border-radius: 60px 90px 30px 30px;
    background: radial-gradient(ellipse at 50% 55%, #d8221c 0%, #a51512 55%, rgba(90, 10, 10, 0) 80%);
  }
</style>
</head>
<body>
  <section class="insert">
    <svg class="insert__waves" viewBox="0 0 1116 516" aria-hidden="true">
      <path d="M0 330 C 260 430, 650 430, 1116 360 L1116 516 L0 516 Z" fill="var(--red-deep)"/>
      <path d="M0 370 C 240 470, 620 480, 1116 420 L1116 516 L0 516 Z" fill="var(--red-mid)"/>
      <path d="M0 440 C 320 505, 720 500, 1116 455 L1116 516 L0 516 Z" fill="var(--red-light)" opacity="0.75"/>
      <path d="M380 516 C 600 470, 850 440, 1116 430 L1116 516 Z" fill="var(--red-deep)" opacity="0.55"/>
    </svg>

    <h1 class="headline headline--free">FREE</h1>
    <h2 class="headline headline--offer">OIL CHANGE</h2>

    <address class="dealer-contact">
      Pinecrest Motor Lending<br>
      2386 Birchwood Avenue<br>
      Lakeview, OH 44190<br>
      216-555-0187
    </address>

    <div class="dealer-brand">
      <span class="dealer-brand__mark"></span>
      <span class="dealer-brand__name">Pinecrest Motor Lending</span>
    </div>

    <div class="address-window">
      <div class="address-window__line"></div>
      <div class="address-window__line"></div>
      <div class="address-window__line"></div>
    </div>

    <div class="vehicle-photo" role="img" aria-label="Photo of a red convertible sports car parked at an angle"></div>
  </section>
</body>
</html>
```